Brick pressure cleaning business needs business cards that are memorable

The business is called Foremost jetstream brick and pressure cleaning.
we blast bricks on new houses and driveways. I would like a logo with water spraying out of the letter s in the wording. Also bricks on the card somehow and maybe the word foremost to be on an angle above the rest of the business name if possible. some shinny gold would be nice somewhere to. Would like to list our services on the back of card- red and cream brick clean, green stain removal, floor scrapes, fence panel clean or changeout. Driveway cleans. hard surface pressure cleans.

Target Market(s)

Building companies and home reno people

Industry/Entity Type

construction

Contact Information for Business Card

business name,phone,number my name, services on the back

Colors
0054AA
0677BA
7BADD7
CADEEF
E8F1F8
FFF300
FFF600
FEFA6F
FFFEC7
FFFEE8

```html
<!DOCTYPE html>
<html lang="en">
<head>
<meta charset="utf-8">
<title>Foremost Jetstream Business Cards</title>
<link rel="stylesheet" href="https://fonts.googleapis.com/css2?family=Poppins:wght@400;500;700&display=swap">
<style>
  :root {
    --bg: #2a2522;
    --card: #1c1c1d;
    --blue: #0b5cad;
    --orange: #f7941d;
    --text: #e9e9e9;
  }
  * { box-sizing: border-box; margin: 0; padding: 0; }
  html, body { width: 1200px; height: 842px; overflow: hidden; }
  body {
    background: var(--bg);
    font-family: "Poppins", sans-serif;
    color: var(--text);
    position: relative;
  }
  .card {
    position: absolute;
    top: 266px;
    width: 540px;
    height: 310px;
    background: var(--card);
    overflow: hidden;
    box-shadow: 0 14px 30px rgba(0,0,0,.45);
  }
  .card--front { left: 40px; }
  .card--back { left: 620px; }

  /* front */
  .band { position: absolute; left: 0; right: 0; height: 14px; background: var(--blue); }
  .band--top { top: 0; }
  .band--bottom { bottom: 0; }
  .contact {
    position: absolute; inset: 0;
    display: flex; flex-direction: column; align-items: center; justify-content: center;
    text-align: center; text-transform: uppercase;
  }
  .contact__name { color: var(--orange); font-weight: 700; font-size: 25px; line-height: 1.05; letter-spacing: .5px; }
  .contact__role { font-size: 15px; line-height: 1.2; letter-spacing: .5px; }
  .divider { width: 70px; height: 2px; background: var(--orange); margin: 10px 0; }
  .contact__line { font-size: 15px; line-height: 1.2; letter-spacing: .3px; }
  .contact__phone { font-size: 18px; }
  .contact__address { margin-top: 14px; }

  /* back */
  .accent { position: absolute; width: 56px; height: 90px; }
  .accent__block { position: absolute; top: 0; width: 44px; height: 100%; background: var(--blue); }
  .accent__line { position: absolute; top: 0; width: 5px; height: 100%; background: var(--orange); }
  .accent--left { left: 0; top: 120px; }
  .accent--left .accent__block { left: 0; }
  .accent--left .accent__line { left: 50px; }
  .accent--right { right: 0; top: 40px; }
  .accent--right .accent__block { right: 0; }
  .accent--right .accent__line { right: 50px; }

  .brand {
    position: absolute; left: 120px; top: 40px;
    display: flex; align-items: center; gap: 14px;
  }
  .brand__mark { width: 62px; height: 62px; border: 3px solid var(--blue); flex: none; }
  .brand__name {
    color: var(--blue); font-weight: 500; text-transform: uppercase;
    font-size: 15px; line-height: 1.25; letter-spacing: 1px; width: 230px;
  }
  .services {
    position: absolute; left: 150px; top: 132px;
    list-style: none; font-size: 14.5px; line-height: 1.45;
  }
  .services li { display: flex; align-items: center; gap: 12px; }
  .services li::before {
    content: ""; width: 12px; height: 6px; background: var(--orange); flex: none;
  }
</style>
</head>
<body>
  <section class="card card--front" aria-label="Business card front">
    <div class="band band--top"></div>
    <div class="contact">
      <p class="contact__name">Daniel Harper</p>
      <p class="contact__role">Managing Director</p>
      <div class="divider"></div>
      <p class="contact__line contact__phone">044-555 018 246</p>
      <p class="contact__line">info@foremostjet.com</p>
      <p class="contact__line">www.foremostjet.com</p>
      <div class="divider"></div>
      <p class="contact__line contact__address">17, Kiln Street Brickfield</p>
      <p class="contact__line">38817, Southvale</p>
    </div>
    <div class="band band--bottom"></div>
  </section>

  <section class="card card--back" aria-label="Business card back">
    <div class="accent accent--left"><span class="accent__block"></span><span class="accent__line"></span></div>
    <div class="accent accent--right"><span class="accent__block"></span><span class="accent__line"></span></div>
    <div class="brand">
      <div class="brand__mark"></div>
      <p class="brand__name">Foremost jetstream brick and pressure cleaning</p>
    </div>
    <ul class="services">
      <li>Red and cream brick clean</li>
      <li>Green stain removal</li>
      <li>Floor scrapes</li>
      <li>Fence panel clean or changeout</li>
      <li>Driveway cleans</li>
      <li>Hard surface pressure cleans</li>
    </ul>
  </section>
</body>
</html>
```